Bref créative
FXK-TWO Business Cards and Stationery
Paintless Dent Repair
Modern
Calvin t Moss
Owner-Technician
4172 Salvia ln
riverside ca 91734
glowmenderfxk7@mailvista.example
repair dings dents hail damage
20 years experience master craftsman

```html
<!DOCTYPE html>
<html lang="en">
<head>
<meta charset="utf-8">
<title>FXK-TWO Business Cards</title>
<link rel="stylesheet" href="https://fonts.googleapis.com/css2?family=Open+Sans:wght@400;600;800&display=swap">
<style>
  :root {
    --bg: #e9e4dc;
    --card: #ffffff;
    --red: #d3232a;
    --ink: #2b2b2b;
    --grey: #7a7a7a;
    --shadow: rgba(60, 40, 20, 0.18);
  }
  * { margin: 0; padding: 0; box-sizing: border-box; }
  html, body { width: 1200px; height: 629px; overflow: hidden; }
  body {
    background: var(--bg);
    font-family: "Open Sans", sans-serif;
    color: var(--ink);
    position: relative;
  }
  .card {
    position: absolute;
    top: 171px;
    width: 500px;
    height: 286px;
    background: var(--card);
    box-shadow: 0 6px 18px var(--shadow);
    overflow: hidden;
  }
  .card--front { left: 70px; }
  .card--back { left: 630px; }

  .brand-name {
    font-weight: 800;
    color: var(--red);
    letter-spacing: 1px;
    line-height: 1;
  }
  .card--front .brand {
    position: absolute;
    left: 0; right: 0; top: 98px;
    text-align: center;
  }
  .card--front .brand-name { font-size: 62px; }
  .brand-tagline {
    margin-top: 10px;
    font-size: 9px;
    color: var(--grey);
    letter-spacing: 0.3px;
  }

  .card--back .brand {
    position: absolute;
    left: 30px; top: 70px;
  }
  .card--back .brand-name { font-size: 40px; }
  .card--back .brand-tagline { font-size: 7px; margin-top: 7px; }

  .owner {
    position: absolute;
    right: 34px; top: 128px;
    text-align: right;
  }
  .owner-name { font-size: 15px; font-weight: 600; color: var(--red); }
  .owner-role { font-size: 10px; color: var(--grey); margin-top: 2px; }

  .contact {
    position: absolute;
    left: 30px; bottom: 22px;
    list-style: none;
    font-size: 9px;
    color: var(--ink);
  }
  .contact li {
    display: flex;
    align-items: center;
    gap: 7px;
    margin-top: 4px;
  }
  .contact svg { width: 11px; height: 11px; flex: none; }
  .edge-band {
    position: absolute;
    right: 0; bottom: 0;
    width: 10px; height: 120px;
    background: var(--red);
  }
</style>
</head>
<body>
  <section class="card card--front" aria-label="Card front">
    <div class="brand">
      <div class="brand-name">FXK-TWO</div>
      <p class="brand-tagline">Repair dings, dents &amp; hail damage · 20 years experience</p>
    </div>
  </section>

  <section class="card card--back" aria-label="Card back">
    <div class="brand">
      <div class="brand-name">FXK-TWO</div>
      <p class="brand-tagline">Repair dings, dents &amp; hail damage · 20 years experience</p>
    </div>

    <div class="owner">
      <p class="owner-name">Calvin t Moss</p>
      <p class="owner-role">Owner-Technician</p>
    </div>

    <ul class="contact">
      <li>
        <svg viewBox="0 0 12 12"><circle cx="6" cy="6" r="6" fill="var(--red)"/><path d="M6 2.5a2 2 0 0 0-2 2c0 1.6 2 4.5 2 4.5s2-2.9 2-4.5a2 2 0 0 0-2-2z" fill="#fff"/></svg>
        <span>4172 Salvia ln</span>
      </li>
      <li>
        <svg viewBox="0 0 12 12"><circle cx="6" cy="6" r="6" fill="var(--red)"/><circle cx="6" cy="6" r="1.6" fill="#fff"/></svg>
        <span>riverside ca 91734</span>
      </li>
      <li>
        <svg viewBox="0 0 12 12"><circle cx="6" cy="6" r="6" fill="var(--red)"/><path d="M4 3l1.3 0 .6 1.6-.8.6a4 4 0 0 0 1.7 1.7l.6-.8 1.6.6 0 1.3C7 8.5 3.5 5 4 3z" fill="#fff"/></svg>
        <span>951-555-0148</span>
      </li>
      <li>
        <svg viewBox="0 0 12 12"><circle cx="6" cy="6" r="6" fill="var(--red)"/><rect x="3" y="4" width="6" height="4" fill="#fff"/><path d="M3 4l3 2.2L9 4" stroke="var(--red)" stroke-width=".7" fill="none"/></svg>
        <span>glowmenderfxk7@mailvista.example</span>
      </li>
      <li>
        <svg viewBox="0 0 12 12"><circle cx="6" cy="6" r="6" fill="var(--red)"/><circle cx="6" cy="6" r="3" fill="none" stroke="#fff" stroke-width=".8"/><path d="M3 6h6M6 3v6" stroke="#fff" stroke-width=".6"/></svg>
        <span>fxktwo.example</span>
      </li>
    </ul>

    <div class="edge-band"></div>
  </section>
</body>
</html>
```